real esate business card with company logo and name

we need a business card design for a real esate company

The company name is Walsh & Brody Pty Ltd, and we have our logo designed and will upload. We want classic or moden feel. Black or white background. looks more textured. Should include folowinginformations
Paul Walsh and Lucy Brody
Sales Agents & Onsite Manager
p: 07 5948 2063
F: 07 5948 2174
M:0461 857 239
3/42 Marlin Crescent, ELLEN GROVE QLD 4078

We want this business card looks professonal. Thank you in advance.

Industry/Entity Type

Real Estate Agent

Contact Information for Business Card

Paul Walsh and Lucy Brody
Onsite Manager & Sales Agents
p: 07 5948 2063
M:0461 857 239

Font styles to use
Serif

Colors
000000
fbfbfb
333333
959595

Requirements
Must have
• company logo and name, black or white back ground

```html
<!DOCTYPE html>
<html lang="en">
<head>
<meta charset="utf-8">
<title>Walsh &amp; Brody Pty Ltd — Business Card</title>
<link href="https://fonts.googleapis.com/css2?family=Lato:wght@400;700&family=Oswald:wght@400&display=swap" rel="stylesheet">
<style>
  :root {
    --stage: #3a3a3a;
    --black: #000000;
    --white: #fbfbfb;
    --charcoal: #333333;
    --grey: #959595;
    --grey-mid: #6b6b6b;
  }
  * { box-sizing: border-box; margin: 0; padding: 0; }
  html, body {
    width: 1200px; height: 1086px; overflow: hidden;
    background: var(--stage);
    font-family: "Lato", sans-serif;
  }
  .card {
    position: absolute; left: 254px;
    width: 677px; height: 387px;
    background: var(--black);
    overflow: hidden;
  }
  .card--front { top: 126px; }
  .card--back { top: 586px; }
  .front-shape { position: absolute; inset: 0; }
  .brand {
    position: absolute; display: flex; flex-direction: column; align-items: center;
  }
  .card--front .brand { left: 0; width: 300px; top: 118px; }
  .card--back .brand { left: 0; width: 677px; top: 118px; }
  .brand__mark { width: 110px; height: 110px; background: var(--grey); }
  .card--back .brand__mark { background: var(--grey-mid); }
  .brand__name {
    margin-top: 36px; font-size: 14px; letter-spacing: 0.5px;
    color: var(--charcoal); white-space: nowrap;
  }
  .card--back .brand__name {
    margin-top: 26px; font-family: "Oswald", sans-serif; font-size: 17px;
    color: var(--grey); letter-spacing: 0.6px;
  }
  .details { position: absolute; left: 370px; top: 72px; color: var(--white); }
  .details__name { font-size: 30px; font-weight: 700; line-height: 1.1; padding-left: 4px; }
  .details__role { font-size: 24px; line-height: 1.2; padding-left: 4px; }
  .contact { list-style: none; margin-top: 26px; }
  .contact li {
    display: flex; align-items: center; gap: 6px;
    font-size: 22px; line-height: 25.5px;
  }
  .contact svg { width: 18px; height: 18px; fill: var(--white); }
  .address { margin-top: 24px; font-size: 22px; line-height: 25px; }
</style>
</head>
<body>
  <section class="card card--front">
    <svg class="front-shape" viewBox="0 0 677 387" preserveAspectRatio="none" aria-hidden="true">
      <path d="M0 0 H252 Q340 194 270 387 H0 Z" fill="#6b6b6b"/>
      <path d="M0 0 H248 Q318 194 242 387 H0 Z" fill="#ffffff"/>
      <path d="M252 0 Q340 194 270 387" fill="none" stroke="#ffffff" stroke-width="1.5"/>
    </svg>
    <div class="brand">
      <div class="brand__mark"></div>
      <p class="brand__name">WALSH &amp; BRODY PTY LTD.</p>
    </div>
    <div class="details">
      <h1 class="details__name">Paul Walsh</h1>
      <p class="details__role">Sales Agents</p>
      <ul class="contact">
        <li><svg viewBox="0 0 18 18"><path d="M5 1h8a1 1 0 0 1 1 1v14a1 1 0 0 1-1 1H5a1 1 0 0 1-1-1V2a1 1 0 0 1 1-1zm1 2v10h6V3zm3 11.2a.9.9 0 1 0 0 1.8.9.9 0 0 0 0-1.8z"/></svg>0461 857 239</li>
        <li><svg viewBox="0 0 18 18"><path d="M1 7c0-2 4-3 8-3s8 1 8 3v1h-4V6.5H5V8H1zm3 2h10l2 6H2zm5 1.5a2 2 0 1 0 0 4 2 2 0 0 0 0-4z"/></svg>07 5948 2063</li>
        <li><svg viewBox="0 0 18 18"><path d="M5 2h8v4H5zM2 7h14v6h-3v3H5v-3H2zm4 4v4h6v-4z"/></svg>07 5948 2174</li>
      </ul>
      <p class="address">3/42 Marlin Crescent<br>HARLOW PARK QLD 4512</p>
    </div>
  </section>

  <section class="card card--back">
    <div class="brand">
      <div class="brand__mark"></div>
      <p class="brand__name">WALSH &amp; BRODY PTY LTD.</p>
    </div>
  </section>
</body>
</html>
```